Flyer-Design für Fitness
Sehr angaschierte Designerin, bin begeistert! Hat sofort alles umgesetzt wie wir es haben wollten. Sehr zu Empfehlen. Vielen dank an Marta
Zielgruppe
Wir haben uns zum Ziel gesetzt, unsere Kunden individuell, professionell und in einem angenehmen Ambiente 'in form' zu bringen.
Stundenlange Workouts waren gestern. Nutzen Sie heute die zeitsparenden Methoden von EMS, VIBRO DECK und KLU Training in Begleitung mit Persönlicher Betreuung, um ihre Ziele zu erreichen. Unsere Zielgruppe sind Männer und Frauen jeden Alters, die Wert auf ihr äußeres legen und sich gesund und fit halten wollen.
Homepage: www.trainingsraum-beispielort.de
Aufgabenstellung
Wir trainieren mit Vibro Deck, Swift Pulse Wear und KLU.
Der soll ein einmal Klapp Flyer sein.

```html
<!DOCTYPE html>
<html lang="de">
<head>
<meta charset="utf-8">
<title>Kernzeit Fitness – Flyer</title>
<link rel="stylesheet" href="https://fonts.googleapis.com/css2?family=Montserrat:wght@500;800;900&display=swap">
<style>
  :root {
    --stage: #e8e8e8;
    --paper: #f4f4f4;
    --brand-green: #84b322;
    --type-dark: #5e9220;
    --type-pale: #c4dc9c;
    --white: #ffffff;
    --photo-top: #2a2a2a;
    --photo-bottom: #4a4a4a;
  }
  * { margin: 0; padding: 0; box-sizing: border-box; }
  html, body {
    width: 1200px; height: 1200px; overflow: hidden;
    background: var(--stage);
    font-family: "Montserrat", sans-serif;
  }
  .flyer {
    position: absolute; left: 315px; top: 45px;
    width: 570px; height: 1110px;
    background: var(--paper);
    overflow: hidden;
  }
  .flyer__panel {
    position: absolute; left: 62px; top: 70px; right: 40px; bottom: 120px;
    background: var(--brand-green);
    overflow: hidden;
  }
  .brand {
    position: absolute; left: 0; right: 0; top: 90px;
    text-align: center;
    color: var(--white);
    font-weight: 500; font-size: 38px; line-height: 1;
  }
  .claims {
    position: absolute; left: 24px; top: 235px;
    transform: rotate(-9deg); transform-origin: left top;
    font-weight: 900; font-size: 28px; line-height: 1.05;
    text-transform: uppercase; white-space: nowrap;
  }
  .claims__line { display: block; }
  .claims__line--dark { color: var(--type-dark); }
  .claims__line--pale { color: var(--type-pale); }
  .claims__line--indent { margin-left: 20px; }
  .photo {
    position: absolute; left: 40px; top: 680px; width: 230px; height: 430px;
    background: linear-gradient(180deg, var(--photo-top), var(--photo-bottom));
    border-radius: 100px 110px 0 0;
  }
  .web {
    position: absolute; right: 58px; bottom: 150px;
    color: var(--white); font-weight: 800; font-size: 18px;
  }
</style>
</head>
<body>
  <main class="flyer">
    <div class="flyer__panel">
      <p class="brand">Kernzeit Fitness</p>
      <div class="claims">
        <span class="claims__line claims__line--dark">EMS HEALTH</span>
        <span class="claims__line claims__line--pale claims__line--indent">VIBRO ATHLETIK</span>
        <span class="claims__line claims__line--pale">DECK TRAINING</span>
        <span class="claims__line claims__line--dark claims__line--indent">KLU SPORT</span>
        <span class="claims__line claims__line--pale">TRAINING FITNESS</span>
        <span class="claims__line claims__line--dark claims__line--indent">EMS HEALTH</span>
        <span class="claims__line claims__line--pale">VIBRO ATHLETIK</span>
        <span class="claims__line claims__line--pale claims__line--indent">DECK TRAINING</span>
        <span class="claims__line claims__line--dark">KLU SPORT</span>
        <span class="claims__line claims__line--pale claims__line--indent">TRAINING</span>
      </div>
    </div>
    <div class="photo" role="img" aria-label="Foto: lächelnde Frau im schwarzen EMS-Trainingsanzug, Hände in den Hüften"></div>
    <p class="web">www.kernzeit-training.de</p>
  </main>
</body>
</html>
```